Flyer für mobile tierärztliche Ultraschalluntersuchungen
Zielgruppe
Mobile tierärztliche Ultraschalluntersuchungen, Zielgruppe: Tierärzt/Tierpraxen, die kein ultraschall Gerät od US-Kenntnisse haben.
Aufgabenstellung
1 Seite (recto D, verso F Sprache), professionell , seriös, aber optisch auffällig, damit es nicht direkt in Papierkorb landet.

```html
<!DOCTYPE html>
<html lang="fr">
<head>
<meta charset="utf-8">
<title>Dr. med. vet. Lina Marest – Échographie vétérinaire itinérante</title>
<link rel="stylesheet" href="https://fonts.googleapis.com/css2?family=Fira+Sans:wght@500;600&family=Open+Sans:wght@400;700&family=Fira+Sans+Condensed:wght@500&display=swap">
<style>
  :root {
    --green-bg: #8cbb6f;
    --green-dark: #4a6e34;
    --green-text: #3f5f2c;
    --panel: #dde8c9;
    --panel-light: #e7efd9;
    --yellow: #fdf3a0;
    --white: #ffffff;
    --ink: #1d1d1b;
  }
  * { margin: 0; padding: 0; box-sizing: border-box; }
  html, body { width: 846px; height: 1200px; overflow: hidden; }
  body { background: var(--green-bg); font-family: "Open Sans", Arial, sans-serif; color: var(--ink); }
  .flyer { position: relative; width: 846px; height: 1200px; overflow: hidden; background: var(--green-bg); }

  .dot { position: absolute; border-radius: 50%; background: var(--yellow); }
  .dot--left { left: -28px; top: 430px; width: 130px; height: 130px; }
  .dot--right { left: 612px; top: 915px; width: 132px; height: 132px; }
  .dot--bottom { left: 108px; top: 1000px; width: 140px; height: 140px; }

  .header-band { position: absolute; left: 0; top: 29px; width: 720px; height: 141px; background: var(--white); }
  .header-band .title { position: absolute; left: 46px; top: 30px; font-family: "Fira Sans", sans-serif; font-weight: 600; color: var(--green-dark); white-space: nowrap; }
  .title .prefix { font-size: 21px; }
  .title .name { font-size: 42px; margin-left: 8px; }
  .header-band .subtitle { position: absolute; left: 46px; top: 88px; font-family: "Fira Sans", sans-serif; font-weight: 600; font-size: 22px; color: var(--green-dark); }

  .portrait { position: absolute; left: 626px; top: -22px; width: 240px; height: 240px; border-radius: 50%; border: 7px solid var(--yellow); background: radial-gradient(circle at 50% 40%, #c9bfb3, #8f8a86 60%, #3c4d6a 100%); }

  .panel { position: absolute; left: 75px; top: 190px; width: 706px; height: 746px; background: var(--panel); border-radius: 12px; }
  .photo-tab { position: absolute; left: 44px; top: 206px; width: 245px; height: 280px; background: var(--panel-light); border-radius: 10px; }
  .photo { position: absolute; left: 56px; top: 218px; width: 222px; height: 258px; border-radius: 6px; background: linear-gradient(160deg, #6e6a70, #3b4356 45%, #c9c6c3 80%, #8b837c); }

  .points { list-style: none; position: absolute; font-size: 19.3px; line-height: 29px; }
  .points li { position: relative; padding-left: 34px; margin-bottom: 6px; }
  .points li svg { position: absolute; left: 0; top: 6px; width: 17px; height: 17px; }
  .points b { font-weight: 700; }
  .points--top { left: 294px; top: 222px; width: 480px; }
  .points--main { left: 130px; top: 497px; width: 620px; }

  .invite { position: absolute; left: 75px; width: 706px; top: 852px; text-align: center; font-family: "Fira Sans", sans-serif; font-weight: 600; font-size: 19px; line-height: 28px; color: var(--green-dark); }

  .brand { position: absolute; left: 187px; top: 917px; width: 471px; height: 161px; background: var(--white); }
  .brand .circle { position: absolute; left: 290px; top: 12px; width: 140px; height: 140px; border-radius: 50%; background: #d4e5c3; }
  .brand .brand-name { position: absolute; left: 12px; top: 34px; font-family: "Fira Sans Condensed", sans-serif; font-weight: 500; font-size: 35px; color: var(--green-text); white-space: nowrap; }
  .brand .brand-tag { position: absolute; left: 12px; top: 86px; font-family: "Fira Sans Condensed", sans-serif; font-weight: 500; font-size: 35px; color: var(--green-text); }
  .brand .rule { position: absolute; left: 10px; right: 10px; bottom: 12px; height: 1.5px; background: var(--green-text); }

  .contact { position: absolute; left: 0; width: 846px; top: 1090px; text-align: center; font-family: "Fira Sans", sans-serif; font-weight: 600; font-size: 19.5px; line-height: 27px; color: var(--white); }
</style>
</head>
<body>
<main class="flyer">
  <div class="dot dot--left"></div>
  <div class="dot dot--right"></div>
  <div class="dot dot--bottom"></div>

  <header class="header-band">
    <h1 class="title"><span class="prefix">Dr. med. vet.</span><span class="name">Lina Marest</span></h1>
    <p class="subtitle">Service itinérant d’ECHOGRAPHIE vétérinaire</p>
  </header>
  <div class="portrait" role="img" aria-label="Portrait de la vétérinaire"></div>

  <section class="panel"></section>
  <div class="photo-tab"></div>
  <div class="photo" role="img" aria-label="La vétérinaire réalisant une échographie sur un chat"></div>

  <ul class="points points--top">
    <li><svg viewBox="0 0 20 20"><circle cx="10" cy="10" r="8.5" fill="none" stroke="#1d1d1b" stroke-width="2"/><path d="M5.5 10h8M10.5 6.5L14 10l-3.5 3.5" fill="none" stroke="#1d1d1b" stroke-width="2.2"/></svg>Diplômée de <b>l’Université de Valmont</b> en <b>2007</b></li>
    <li><svg viewBox="0 0 20 20"><circle cx="10" cy="10" r="8.5" fill="none" stroke="#1d1d1b" stroke-width="2"/><path d="M5.5 10h8M10.5 6.5L14 10l-3.5 3.5" fill="none" stroke="#1d1d1b" stroke-width="2.2"/></svg>Doctorat en pathologie de la faune sauvage</li>
    <li><svg viewBox="0 0 20 20"><circle cx="10" cy="10" r="8.5" fill="none" stroke="#1d1d1b" stroke-width="2"/><path d="M5.5 10h8M10.5 6.5L14 10l-3.5 3.5" fill="none" stroke="#1d1d1b" stroke-width="2.2"/></svg>Ayant plus de <b>10 ans de pratique clinique</b> (animaux de compagnie et NACs)</li>
    <li><svg viewBox="0 0 20 20"><circle cx="10" cy="10" r="8.5" fill="none" stroke="#1d1d1b" stroke-width="2"/><path d="M5.5 10h8M10.5 6.5L14 10l-3.5 3.5" fill="none" stroke="#1d1d1b" stroke-width="2.2"/></svg>Suivant des <b>formations continues</b> en échographie en Suisse et à l’étranger</li>
    <li><svg viewBox="0 0 20 20"><circle cx="10" cy="10" r="8.5" fill="none" stroke="#1d1d1b" stroke-width="2"/><path d="M5.5 10h8M10.5 6.5L14 10l-3.5 3.5" fill="none" stroke="#1d1d1b" stroke-width="2.2"/></svg>La prise de rendez-vous est <b>flexible et rapide</b> par email ou téléphone</li>
  </ul>

  <ul class="points points--main">
    <li><svg viewBox="0 0 20 20"><circle cx="10" cy="10" r="8.5" fill="none" stroke="#1d1d1b" stroke-width="2"/><path d="M5.5 10h8M10.5 6.5L14 10l-3.5 3.5" fill="none" stroke="#1d1d1b" stroke-width="2.2"/></svg><b>Je me déplace avec</b> mon échographe de haute qualité <b>Sonalis</b> active pour des échographie abdominales et thoraciques <b>à votre cabinet</b></li>
    <li><svg viewBox="0 0 20 20"><circle cx="10" cy="10" r="8.5" fill="none" stroke="#1d1d1b" stroke-width="2"/><path d="M5.5 10h8M10.5 6.5L14 10l-3.5 3.5" fill="none" stroke="#1d1d1b" stroke-width="2.2"/></svg><b>Vos clients restent chez vous,</b> pas de route à faire et a facturation se fait par votre cabinet</li>
    <li><svg viewBox="0 0 20 20"><circle cx="10" cy="10" r="8.5" fill="none" stroke="#1d1d1b" stroke-width="2"/><path d="M5.5 10h8M10.5 6.5L14 10l-3.5 3.5" fill="none" stroke="#1d1d1b" stroke-width="2.2"/></svg>Je m’occupe des chiens et de chats, mais aussi des NACs, incl. reptiles</li>
    <li><svg viewBox="0 0 20 20"><circle cx="10" cy="10" r="8.5" fill="none" stroke="#1d1d1b" stroke-width="2"/><path d="M5.5 10h8M10.5 6.5L14 10l-3.5 3.5" fill="none" stroke="#1d1d1b" stroke-width="2.2"/></svg>Nous pouvons <b>discuter et échanger</b> pour la prise en charge de votre patient</li>
    <li><svg viewBox="0 0 20 20"><circle cx="10" cy="10" r="8.5" fill="none" stroke="#1d1d1b" stroke-width="2"/><path d="M5.5 10h8M10.5 6.5L14 10l-3.5 3.5" fill="none" stroke="#1d1d1b" stroke-width="2.2"/></svg>Je parle quatre langues et les rapports peuvent se faire en français, allemand ou anglais</li>
  </ul>

  <p class="invite">Vous êtes curieux ?<br>Rencontrons-nous pour discuter!</p>

  <div class="brand">
    <div class="circle"></div>
    <div class="brand-name">Dr. med. vet. Lina Marest</div>
    <div class="brand-tag">sonovet mobile</div>
    <div class="rule"></div>
  </div>

  <footer class="contact">
    Tél : +41 79 000 12 34<br>
    Email: lmarest.veterinaire@exemple.ch<br>
    www.sonovet-mobile.ch
  </footer>
</main>
</body>
</html>
```